Pregnancy Wellbeing Coach seeks Book Cover Design

I am a former midwife who now works within alternative healthcare to support women and their families during pregnancy.
I have written a book "Quiet and Carrying Light" which is a pregnancy guide that encourages women to look "outside the box" of conventional medicine ...to find alternative solutions to difficulties that they might be experiencing. So it looks as breathing, meditative and journeying techniques, exercise, connection to nature, communication with the baby...those sort of things.
The book also is a guide for those who support the pregnant women ...the best friend, sister, mother, partner - all those who want to be involved and make a positive contribution to the transformation of the woman into motherhood ...because undoubtedly their lives will be changed by the experience.
It is my belief that we all hold an innate wisdom, the wisdom of our ancestors and that during pregnancy women are connected to the lineage of child bearers back through time ...so it is has a sacred element to it, a time of coming together ... a passing through a doorway, where life will be forever changed.
My website is : www.maevelorrimerwellbeing.example

Thank you :)

Target Market(s)

Pregnant women and those who support them during pregnancy

Industry/Entity Type

Health Care

Font styles to use
Serif
Script

Colors

Designer to choose colors to be used in the design.

Requirements
Must have
• A pregnant woman ...
• Natural World
• Title : Quiet & Carrying Light
• Subtitle : Gentle Practices to Guide A Present-Day Mother's Changing Passage Across the Months of Waiting
• Author: Maeve Lorrimer
Nice to have
• I have a feeling that nature or the natural world is important.
• And the sign of support/community
• And maybe the stars
Should not have
• No Babies
• No "highly polished women"
• No huge pregnant bellies

```html
<!DOCTYPE html>
<html lang="en">
<head>
<meta charset="utf-8">
<title>Quiet &amp; Carrying Light — Book Cover</title>
<link rel="stylesheet" href="https://fonts.googleapis.com/css2?family=Playfair+Display:ital,wght@0,400;0,500;1,400&family=Montserrat:wght@600&display=swap">
<style>
  :root {
    --page-bg: #ffffff;
    --sky-top: #e4f3f7;
    --sky-mid: #eaf2fa;
    --haze-pink: #efc6ea;
    --sun-glow: #fff8dc;
    --horizon: #9fb8dc;
    --sea-light: #3b78b0;
    --sea-mid: #22508f;
    --sea-deep: #0e2350;
    --figure-light: #f3eef4;
    --figure-mid: #c9b6c8;
    --figure-shade: #8fa7c9;
    --title-purple: #7b2585;
    --subtitle-ink: #1d1a24;
    --author-white: #ffffff;
  }
  * { margin: 0; padding: 0; box-sizing: border-box; }
  html, body {
    width: 1200px; height: 1200px; overflow: hidden;
    background: var(--page-bg);
  }
  .canvas {
    position: relative; width: 1200px; height: 1200px;
    display: flex; align-items: center; justify-content: center;
  }
  .book-cover {
    position: relative; width: 747px; height: 1120px; overflow: hidden;
  }
  .cover-art { position: absolute; inset: 0; width: 100%; height: 100%; }
  .figure-photo {
    position: absolute; left: 168px; top: 520px; width: 200px; height: 430px;
  }
  .title-block {
    position: absolute; top: 70px; left: 0; right: 0;
    text-align: center; color: var(--title-purple);
    font-family: "Playfair Display", serif;
  }
  .title-lead {
    display: block;
    font-size: 72px; font-weight: 500; line-height: 1; letter-spacing: -0.5px;
  }
  .title-main {
    display: block;
    font-size: 176px; font-weight: 400; line-height: 1;
    letter-spacing: 22px; margin-top: 6px; padding-left: 22px;
  }
  .title-rule {
    width: 500px; height: 2px; margin: 26px auto 0;
    background: var(--title-purple);
  }
  .subtitle {
    position: absolute; top: 372px; left: 60px; right: 60px;
    text-align: center; color: var(--subtitle-ink);
    font-family: "Playfair Display", serif; font-style: italic;
    font-size: 31px; line-height: 1.28;
  }
  .author {
    position: absolute; bottom: 48px; left: 0; right: 0;
    text-align: center; color: var(--author-white);
    font-family: "Montserrat", sans-serif; font-weight: 600;
    font-size: 46px; letter-spacing: 4px;
  }
</style>
</head>
<body>
<main class="canvas">
  <section class="book-cover">
    <svg class="cover-art" viewBox="0 0 747 1120" preserveAspectRatio="none"
         role="img" aria-label="Starlit sea at sunrise under a pastel sky">
      <defs>
        <linearGradient id="sky-sea" x1="0" y1="0" x2="0" y2="1">
          <stop offset="0" stop-color="var(--sky-top)"/>
          <stop offset="0.32" stop-color="var(--sky-mid)"/>
          <stop offset="0.48" stop-color="var(--haze-pink)"/>
          <stop offset="0.62" stop-color="var(--horizon)"/>
          <stop offset="0.7" stop-color="var(--sea-light)"/>
          <stop offset="0.85" stop-color="var(--sea-mid)"/>
          <stop offset="1" stop-color="var(--sea-deep)"/>
        </linearGradient>
        <radialGradient id="sun" cx="0.68" cy="0.6" r="0.35">
          <stop offset="0" stop-color="var(--sun-glow)" stop-opacity="1"/>
          <stop offset="0.4" stop-color="var(--sun-glow)" stop-opacity="0.55"/>
          <stop offset="1" stop-color="var(--sun-glow)" stop-opacity="0"/>
        </radialGradient>
        <radialGradient id="water-shimmer" cx="0.75" cy="0.78" r="0.25">
          <stop offset="0" stop-color="#7fe0d6" stop-opacity="0.55"/>
          <stop offset="1" stop-color="#7fe0d6" stop-opacity="0"/>
        </radialGradient>
      </defs>
      <rect width="747" height="1120" fill="url(#sky-sea)"/>
      <rect width="747" height="1120" fill="url(#sun)"/>
      <rect width="747" height="1120" fill="url(#water-shimmer)"/>
    </svg>

    <svg class="figure-photo" viewBox="0 0 200 430"
         role="img" aria-label="Photo of a smiling pregnant woman in a white lace dress standing waist-deep in the sea, hands resting on her belly">
      <defs>
        <linearGradient id="figure-tone" x1="0" y1="0" x2="0" y2="1">
          <stop offset="0" stop-color="var(--figure-mid)" stop-opacity="0.85"/>
          <stop offset="0.35" stop-color="var(--figure-light)" stop-opacity="0.9"/>
          <stop offset="0.8" stop-color="var(--figure-shade)" stop-opacity="0.75"/>
          <stop offset="1" stop-color="var(--figure-shade)" stop-opacity="0"/>
        </linearGradient>
      </defs>
      <rect x="10" y="0" width="180" height="430" rx="90" fill="url(#figure-tone)"/>
    </svg>

    <header class="title-block">
      <h1>
        <span class="title-lead">Quiet &amp; Carrying</span>
        <span class="title-main">LIGHT</span>
      </h1>
      <div class="title-rule"></div>
    </header>

    <p class="subtitle">Gentle Practices to Guide<br>A Present-Day Mother’s Changing Passage<br>Across the Months of Waiting</p>

    <p class="author">MAEVE LORRIMER</p>
  </section>
</main>
</body>
</html>
```